Bref créative
Stationary for telecom company
KLV Telecommunications
Professional
Dinh Quoc Bao
Director
47 Hoa Lu Street, Ward 5, Go Vap District, Ho Chi Minh City
bao.dinh@mrq.net.vn
www.klvtelecom.vn

```html
<!DOCTYPE html>
<html lang="en">
<head>
<meta charset="utf-8">
<title>KLV Telecommunications – Business Card</title>
<link rel="stylesheet" href="https://fonts.googleapis.com/css2?family=Open+Sans:ital,wght@0,400;0,700;1,400&display=swap">
<style>
  :root {
    --backdrop: #e9e6e1;
    --card-white: #ffffff;
    --brand-blue: #2f5f9e;
    --brand-blue-dark: #1f4579;
    --swoosh-black: #1a1a1a;
    --text-grey: #5c5c5c;
    --text-light: #ffffff;
  }
  * { margin: 0; padding: 0; box-sizing: border-box; }
  html, body {
    width: 1200px; height: 914px; overflow: hidden;
    background: var(--backdrop);
    font-family: "Open Sans", Arial, sans-serif;
  }
  .business-card {
    position: absolute; left: 100px; top: 171px;
    width: 1000px; height: 572px;
    background: var(--card-white);
    box-shadow: 0 10px 30px rgba(0,0,0,0.18);
    overflow: hidden;
  }
  .card-band { position: absolute; inset: 0; width: 100%; height: 100%; }
  .brand-name {
    position: absolute; left: 90px; top: 70px;
    font-weight: 700; font-size: 40px; letter-spacing: 0.5px;
    color: var(--brand-blue); line-height: 1;
  }
  .holder { position: absolute; left: 90px; top: 200px; }
  .holder-name { font-style: italic; font-size: 24px; color: var(--brand-blue); }
  .holder-title { font-size: 17px; color: var(--text-grey); margin-top: 6px; }
  .card-address {
    position: absolute; left: 60px; bottom: 50px;
    font-style: italic; font-size: 16px; color: var(--text-light);
  }
  .contact-list {
    position: absolute; left: 700px; top: 400px;
    list-style: none; color: var(--text-light); font-size: 16px;
  }
  .contact-item { display: flex; align-items: center; gap: 10px; height: 30px; }
  .contact-icon { width: 20px; height: 20px; flex: none; }
</style>
</head>
<body>
  <article class="business-card">
    <svg class="card-band" viewBox="0 0 1000 572" preserveAspectRatio="none" aria-hidden="true">
      <path d="M0,372 Q520,470 1000,300 L1000,572 L0,572 Z" fill="var(--brand-blue)"/>
      <path d="M40,330 Q520,450 1000,270 L1000,292 Q520,470 40,330 Z" fill="var(--swoosh-black)"/>
    </svg>

    <div class="brand-name">KLV Telecommunications</div>

    <div class="holder">
      <p class="holder-name">Dinh Quoc Bao</p>
      <p class="holder-title">Director</p>
    </div>

    <p class="card-address">47 Hoa Lu Street, Ward 5, Go Vap District, Ho Chi Minh City</p>

    <ul class="contact-list">
      <li class="contact-item">
        <svg class="contact-icon" viewBox="0 0 20 20"><circle cx="10" cy="10" r="10" fill="#fff"/><path d="M6.5 5.5 l2 -0.5 1 2.5 -1.2 1 a6 6 0 0 0 3 3 l1 -1.2 2.5 1 -0.5 2 a1.5 1.5 0 0 1 -1.6 1 a9 9 0 0 1 -7.2 -7.2 a1.5 1.5 0 0 1 1 -1.6z" fill="var(--brand-blue)"/></svg>
        <span>(84) 8 39 260417</span>
      </li>
      <li class="contact-item">
        <svg class="contact-icon" viewBox="0 0 20 20"><circle cx="10" cy="10" r="10" fill="#fff"/><rect x="5" y="8" width="10" height="6" rx="1" fill="var(--brand-blue)"/><rect x="7" y="5" width="6" height="3" fill="var(--brand-blue)"/></svg>
        <span>(84) 8 39 260588</span>
      </li>
      <li class="contact-item">
        <svg class="contact-icon" viewBox="0 0 20 20"><circle cx="10" cy="10" r="10" fill="#fff"/><rect x="5" y="6.5" width="10" height="7" fill="var(--brand-blue)"/><path d="M5 6.5 L10 10.5 L15 6.5" stroke="#fff" stroke-width="1" fill="none"/></svg>
        <span>bao.dinh@mrq.net.vn</span>
      </li>
      <li class="contact-item">
        <svg class="contact-icon" viewBox="0 0 20 20"><circle cx="10" cy="10" r="10" fill="#fff"/><circle cx="10" cy="10" r="5" stroke="var(--brand-blue)" stroke-width="1.3" fill="none"/><path d="M5 10 H15 M10 5 Q7 10 10 15 M10 5 Q13 10 10 15" stroke="var(--brand-blue)" stroke-width="1" fill="none"/></svg>
        <span>www.klvtelecom.vn</span>
      </li>
    </ul>
  </article>
</body>
</html>
```